Tavor Management - Managing Urban Projects for the City of Modiin

Tavor Management needs a website that projects its professionalism and innovation to the residents of the city of Modiin. The design needs include: 1) a homepage design, 2) ~12 customized icons used on the homepage, 3) a layered image (city landscape with company logo on it) used as a fullwidth background image on the homepage. The client wants a site that is pleasant on the eye and easy to navigate. The client wants the site to project the organization as being professional and innovative.

Target Market(s)

adult residents of the city of modiin, israel

Industry/Entity Type

management of urban projects

Number of Pages Required

1 page

Font styles to use
Sans Serif

Requirements
Must have
• psd of design and psd of main fullwidth background image on the homepage
Nice to have
• icons for navigation bar and homepage teasers
Should not have
• colors should match the logo attached, font should be modern

```html
<!DOCTYPE html>
<html lang="en">
<head>
<meta charset="utf-8">
<title>Tavor Management</title>
<link href="https://fonts.googleapis.com/css2?family=Montserrat:wght@700;800&family=Poppins:wght@400;500;600&family=Roboto:wght@700&display=swap" rel="stylesheet">
<style>
:root{
  --green:#5bb046;
  --green-dark:#4ea33a;
  --ink:#111111;
  --white:#ffffff;
  --grey:#8a8a8a;
  --footer:#000000;
}
*{margin:0;padding:0;box-sizing:border-box}
html,body{width:1200px;height:3196px;overflow:hidden;background:var(--white)}
body{position:relative;font-family:"Poppins",sans-serif;color:var(--ink)}
.abs{position:absolute}

/* hero */
.hero{left:0;top:0;width:1200px;height:680px;background:linear-gradient(180deg,#8b8f88 0%,#6f7b62 30%,#5b6e45 60%,#6f7f55 100%)}
.hero-wave{left:0;top:520px;width:1200px;height:160px}
.brand{left:0;width:1200px;top:120px;text-align:center;display:flex;justify-content:center;align-items:center;gap:12px}
.brand-dot{width:34px;height:34px;border-radius:50%;background:var(--green)}
.brand-name{font-family:"Montserrat",sans-serif;font-weight:800;font-size:28px;color:var(--white);white-space:nowrap}
.hero-title{left:0;width:1200px;top:283px;text-align:center;font-family:"Montserrat",sans-serif;font-weight:800;font-size:45px;line-height:51px;color:var(--white);letter-spacing:.5px}
.btn{display:flex;align-items:center;justify-content:center;background:var(--white);border-radius:24px;font-family:"Roboto",sans-serif;font-weight:700;font-size:15px;color:var(--ink)}
.hero-btn{left:524px;top:420px;width:152px;height:44px}

/* side navigation */
.sidenav{left:1029px;top:0;width:171px;background:var(--green)}
.sidenav a{display:flex;align-items:center;gap:12px;height:68.4px;padding-left:16px;border-bottom:1px solid rgba(255,255,255,.55);color:var(--white);text-decoration:none;font-size:15.5px;line-height:18px}
.sidenav svg{width:26px;height:26px;flex:none}

/* teaser cards */
.card{top:732px;width:189px;height:298px;border-radius:95px;background:var(--white);box-shadow:0 14px 30px rgba(0,0,0,.10);text-align:center}
.card.active{background:var(--green)}
.card-icon{position:absolute;left:52px;top:54px;width:85px;height:85px;border-radius:50%;background:var(--green);display:flex;align-items:center;justify-content:center}
.card.active .card-icon{background:var(--white)}
.card-icon svg{width:46px;height:46px}
.card-label{position:absolute;left:0;width:100%;top:170px;font-family:"Roboto",sans-serif;font-weight:700;font-size:19px;line-height:22px;color:var(--ink)}
.card.active .card-label{color:var(--white)}
.card-arrow{position:absolute;left:75px;bottom:-21px;width:40px;height:40px;border-radius:50%;background:var(--white);box-shadow:0 3px 8px rgba(0,0,0,.12);display:flex;align-items:center;justify-content:center}
.slider-arrow{top:877px;width:32px;height:32px;border-radius:50%;border:1.5px solid var(--green);display:flex;align-items:center;justify-content:center}

/* about */
.about{left:0;top:1144px;width:1200px;height:516px;background:linear-gradient(180deg,#3d4134 0%,#2e3a2a 40%,#2a3326 65%,#3b4036 100%)}
.section-title{font-family:"Montserrat",sans-serif;font-weight:800;font-size:30px}
.about-title{left:0;width:1200px;top:1238px;text-align:center;color:var(--white)}
.about-text{left:92px;width:1016px;top:1306px;text-align:center;color:var(--white);font-size:15.4px;line-height:25.7px}
.about-btn{left:527px;top:1554px;width:146px;height:46px}

/* projects */
.projects-title{left:0;width:1200px;top:1735px;text-align:center;color:var(--green)}
.strip{left:0;top:1819px;width:1200px;height:381px}
.see-btn{left:527px;top:2137px;width:146px;height:44px}

/* contact */
.contact-title{left:109px;top:2277px;color:var(--ink)}
.field{height:42px;background:var(--white);box-shadow:2px 3px 8px rgba(0,0,0,.12);display:flex;align-items:center;justify-content:space-between;padding:0 12px 0 14px;font-size:11px;color:var(--grey)}
.field-icon{width:32px;height:32px;border-radius:50%;border:1.5px solid var(--green);display:flex;align-items:center;justify-content:center}
.send-btn{left:110px;top:2638px;width:241px;height:45px;background:var(--green);color:var(--white);border-radius:24px}
.info{left:726px;display:flex;align-items:center;gap:14px;font-size:20px;color:var(--green-dark);white-space:nowrap}
.info svg{width:30px;height:30px}

/* footer */
.footer-wave{left:0;top:2660px;width:1200px;height:150px}
.footer{left:0;top:2805px;width:1200px;height:391px;background:var(--footer)}
.footer-brand{left:76px;top:2930px;width:210px;text-align:center}
.footer-brand .brand-dot{margin:0 auto 14px;width:70px;height:70px}
.footer-brand .brand-name{font-size:22px}
.social{top:3089px;width:24px;height:24px;border-radius:50%;border:1.5px solid var(--white)}
.foot-head{top:2900px;font-family:"Montserrat",sans-serif;font-weight:800;font-size:21px;color:var(--white)}
.foot-links{top:2951px;list-style:none;color:var(--white);font-size:18px;line-height:31px;letter-spacing:.5px}
.foot-contact{left:795px;color:var(--white);font-size:18px;line-height:24px;display:flex;gap:16px;letter-spacing:.5px}
.foot-contact svg{width:24px;height:24px;flex:none}
.foot-line{left:70px;top:3133px;width:976px;height:1px;background:#6a6a6a}
.copyright{left:0;width:1116px;top:3156px;text-align:center;color:var(--white);font-size:16px;letter-spacing:.5px;font-weight:500}
.to-top{left:1145px;top:3068px;width:36px;height:36px;border-radius:50%;background:var(--green);display:flex;align-items:center;justify-content:center}
</style>
</head>
<body>

<!-- hero -->
<div class="abs hero" role="img" aria-label="Aerial view of the city with residential towers, highway and a green park with a lake"></div>
<svg class="abs hero-wave" viewBox="0 0 1200 160" preserveAspectRatio="none">
  <path d="M0,160 L0,150 C250,140 520,40 780,30 C900,26 980,40 1029,60 L1200,60 L1200,160 Z" fill="#fff"/>
  <path d="M0,152 C260,140 520,40 780,32 C900,28 980,42 1029,62" fill="none" stroke="#5bb046" stroke-width="9"/>
  <path d="M0,130 C300,110 520,20 760,8" fill="none" stroke="#fff" stroke-width="3" opacity=".7"/>
</svg>
<div class="abs brand"><span class="brand-dot"></span><span class="brand-name">Tavor Management</span></div>
<h1 class="abs hero-title">WELCOME TO<br>TAVOR MANAGEMENT.</h1>
<a class="abs btn hero-btn">GET STARTED</a>

<nav class="abs sidenav">
  <a><svg viewBox="0 0 24 24" fill="none" stroke="#fff" stroke-width="1.5"><circle cx="12" cy="12" r="9"/><path d="M3 12h18M12 3c3 3 3 15 0 18M12 3c-3 3-3 15 0 18"/></svg>Language</a>
  <a><svg viewBox="0 0 24 24" fill="none" stroke="#fff" stroke-width="1.5"><path d="M3 11l9-7 9 7M5 9v11h5v-6h4v6h5V9"/></svg>Home</a>
  <a><svg viewBox="0 0 24 24" fill="none" stroke="#fff" stroke-width="1.5"><circle cx="12" cy="12" r="9"/><path d="M12 10v7M12 7v.5"/></svg>About</a>
  <a><svg viewBox="0 0 24 24" fill="none" stroke="#fff" stroke-width="1.5"><path d="M4 20V12M9 20V8M14 20v-6M19 20V4M3 20h18"/></svg>Business<br>Promotion</a>
  <a><svg viewBox="0 0 24 24" fill="none" stroke="#fff" stroke-width="1.5"><circle cx="12" cy="12" r="3.5"/><path d="M12 2v4M12 18v4M2 12h4M18 12h4M5 5l3 3M16 16l3 3M5 19l3-3M16 8l3-3"/></svg>Project<br>Management</a>
  <a><svg viewBox="0 0 24 24" fill="none" stroke="#fff" stroke-width="1.5"><rect x="6" y="6" width="12" height="12" rx="2"/><path d="M9 3v3M15 3v3M9 18v3M15 18v3M3 9h3M3 15h3M18 9h3M18 15h3"/></svg>Tech and<br>Commercial</a>
  <a><svg viewBox="0 0 24 24" fill="none" stroke="#fff" stroke-width="1.5"><rect x="5" y="3" width="14" height="18" rx="1"/><path d="M8 8h8M8 12h8M8 16h5"/></svg>Tenders</a>
  <a><svg viewBox="0 0 24 24" fill="none" stroke="#fff" stroke-width="1.5"><rect x="3" y="4" width="18" height="11" rx="1"/><path d="M12 15v6M8 21h8M6 8h12M6 11h8"/></svg>Signage and<br>Publication</a>
  <a><svg viewBox="0 0 24 24" fill="none" stroke="#fff" stroke-width="1.5"><path d="M3 6h7l2 2h9v11H3z"/></svg>Projects</a>
  <a><svg viewBox="0 0 24 24" fill="none" stroke="#fff" stroke-width="1.5"><path d="M5 4h4l2 5-2.5 1.5a11 11 0 005 5L15 13l5 2v4a2 2 0 01-2 2A16 16 0 013 6a2 2 0 012-2z"/></svg>Contact</a>
</nav>

<!-- teaser cards -->
<div class="abs slider-arrow" style="left:17px"><svg width="14" height="14" viewBox="0 0 14 14"><path d="M9 2L4 7l5 5" fill="none" stroke="#5bb046" stroke-width="1.5"/></svg></div>
<div class="abs slider-arrow" style="left:1151px"><svg width="14" height="14" viewBox="0 0 14 14"><path d="M5 2l5 5-5 5" fill="none" stroke="#5bb046" stroke-width="1.5"/></svg></div>

<div class="abs card" style="left:60px">
  <div class="card-icon"><svg viewBox="0 0 24 24" fill="none" stroke="#fff" stroke-width="1.4"><path d="M8 21V11M8 11c-3 0-4-3-3-6 1-2 5-2 6 0 1 3 0 6-3 6zM3 21h18M13 21v-5h7v5M14 13a3 3 0 015 0M12 11a6 6 0 019 0"/></svg></div>
  <div class="card-label">THE TECHNOLOGY<br>PARK</div>
  <div class="card-arrow"><svg width="22" height="12" viewBox="0 0 22 12"><path d="M1 6h19M15 1l5 5-5 5" fill="none" stroke="#111" stroke-width="1.5"/></svg></div>
</div>
<div class="abs card" style="left:280px">
  <div class="card-icon"><svg viewBox="0 0 24 24" fill="none" stroke="#fff" stroke-width="1.4"><rect x="5" y="3" width="14" height="16" rx="3"/><path d="M5 10h14M5 14h14M8 19v2M16 19v2"/><circle cx="8.5" cy="16.5" r=".8"/><circle cx="15.5" cy="16.5" r=".8"/></svg></div>
  <div class="card-label">TRANSPORTATION<br>CENTER</div>
  <div class="card-arrow"><svg width="22" height="12" viewBox="0 0 22 12"><path d="M1 6h19M15 1l5 5-5 5" fill="none" stroke="#111" stroke-width="1.5"/></svg></div>
</div>
<div class="abs card active" style="left:501px">
  <div class="card-icon"><svg viewBox="0 0 24 24" fill="none" stroke="#111" stroke-width="1.5"><path d="M7 17L17 7M4 17l3 3M6 15l3 3M15 6l3 3M17 4l3 3M3 21l2-2M19 5l2-2"/></svg></div>
  <div class="card-label">MUNICIPAL<br>SPORTS CENTER</div>
  <div class="card-arrow"><svg width="22" height="12" viewBox="0 0 22 12"><path d="M1 6h19M15 1l5 5-5 5" fill="none" stroke="#111" stroke-width="1.5"/></svg></div>
</div>
<div class="abs card" style="left:721px">
  <div class="card-icon"><svg viewBox="0 0 24 24" fill="none" stroke="#fff" stroke-width="1.4"><path d="M12 21V11M12 11c-5 0-7-4-6-8 4 0 7 3 6 8zM12 14c4 0 6-3 6-6-4 0-6 2-6 6zM8 21h8"/></svg></div>
  <div class="card-label">CEDAR<br>PARK</div>
  <div class="card-arrow"><svg width="22" height="12" viewBox="0 0 22 12"><path d="M1 6h19M15 1l5 5-5 5" fill="none" stroke="#111" stroke-width="1.5"/></svg></div>
</div>
<div class="abs card" style="left:942px">
  <div class="card-icon"><svg viewBox="0 0 24 24" fill="none" stroke="#fff" stroke-width="1.4"><path d="M4 21V8l8-5 8 5v13M3 21h18M9 21v-5h6v5M8 10h2M14 10h2M8 13h2M14 13h2"/></svg></div>
  <div class="card-label">LOTEM<br>CENTER</div>
  <div class="card-arrow"><svg width="22" height="12" viewBox="0 0 22 12"><path d="M1 6h19M15 1l5 5-5 5" fill="none" stroke="#111" stroke-width="1.5"/></svg></div>
</div>

<!-- about -->
<section class="abs about" role="img" aria-label="Forested mountains reflected in a calm lake at dusk"></section>
<h2 class="abs section-title about-title">ABOUT US</h2>
<p class="abs about-text">Tavor Management was established in 2014 as a professional body that works to develop the technology park and the Lotem center and turn them into leading centers in the fields of business, commerce, advanced industry and innovative technology while realizing the potential of the centers in order to increase the contribution and economic and employment growth of the city. The directorate also works to develop and promote projects and initiatives in the commercial and employment areas of the city and its assets for the well-being and benefit of the city's residents. In general, the directorate works to promote, plan and develop urban parks and projects. in the field of construction and infrastructure in public projects, manages the municipality's assets and assists in the promotion and management of municipal, governmental and private initiatives, all with the aim of promoting the well-being of the city's residents.</p>
<a class="abs btn about-btn">LEARN MORE</a>

<!-- projects -->
<h2 class="abs section-title projects-title">OUR LATEST PROJECTS</h2>
<svg class="abs strip" viewBox="0 0 1200 381" role="img" aria-label="Project photos: people swimming in the municipal pool, the sports center building and an evening promenade">
  <defs>
    <linearGradient id="p1" x1="0" y1="0" x2="0" y2="1"><stop offset="0" stop-color="#6aa9c8"/><stop offset="1" stop-color="#2f6f9a"/></linearGradient>
    <linearGradient id="p2" x1="0" y1="0" x2="0" y2="1"><stop offset="0" stop-color="#5e7f6c"/><stop offset="1" stop-color="#3a86b3"/></linearGradient>
    <linearGradient id="p3" x1="0" y1="0" x2="0" y2="1"><stop offset="0" stop-color="#cfd6dc"/><stop offset="1" stop-color="#8b9096"/></linearGradient>
    <linearGradient id="p4" x1="0" y1="0" x2="0" y2="1"><stop offset="0" stop-color="#7fb3cf"/><stop offset="1" stop-color="#3b7fa5"/></linearGradient>
    <linearGradient id="p5" x1="0" y1="0" x2="0" y2="1"><stop offset="0" stop-color="#2c3540"/><stop offset="1" stop-color="#a89a86"/></linearGradient>
  </defs>
  <rect width="1200" height="381" fill="#fff"/>
  <polygon points="0,0 273,0 91,381 0,381" fill="url(#p1)"/>
  <polygon points="279,0 561,0 383,381 97,381" fill="url(#p2)"/>
  <polygon points="567,0 629,0 803,381 389,381" fill="url(#p3)"/>
  <polygon points="635,0 921,0 1104,381 809,381" fill="url(#p4)"/>
  <polygon points="927,0 1200,0 1200,381 1110,381" fill="url(#p5)"/>
</svg>
<a class="abs btn see-btn">SEE ALL</a>

<!-- contact -->
<h2 class="abs section-title contact-title">CONTACT US</h2>
<div class="abs field" style="left:115px;top:2374px;width:254px">Tavor Management<span class="field-icon"><svg width="18" height="18" viewBox="0 0 24 24" fill="none" stroke="#5bb046" stroke-width="1.8"><circle cx="12" cy="8" r="4"/><path d="M4 21a8 8 0 0116 0"/></svg></span></div>
<div class="abs field" style="left:410px;top:2374px;width:253px">Tavor Management<span class="field-icon"><svg width="18" height="18" viewBox="0 0 24 24" fill="none" stroke="#5bb046" stroke-width="1.8"><rect x="3" y="6" width="18" height="12"/><path d="M3 6l9 7 9-7"/></svg></span></div>
<div class="abs field" style="left:115px;top:2455px;width:254px">08-9120456<span class="field-icon"><svg width="18" height="18" viewBox="0 0 24 24" fill="none" stroke="#5bb046" stroke-width="1.8"><path d="M5 4h4l2 5-2.5 1.5a11 11 0 005 5L15 13l5 2v4a2 2 0 01-2 2A16 16 0 013 6a2 2 0 012-2z"/></svg></span></div>
<div class="abs field" style="left:410px;top:2455px;width:253px">MM/dd/YY<span class="field-icon"><svg width="18" height="18" viewBox="0 0 24 24" fill="none" stroke="#5bb046" stroke-width="1.8"><rect x="4" y="5" width="16" height="15"/><path d="M4 10h16M8 3v4M16 3v4"/></svg></span></div>
<div class="abs field" style="left:115px;top:2550px;width:548px">Tavor Management<svg width="14" height="14" viewBox="0 0 14 14"><path d="M3 5l4 4 4-4" fill="none" stroke="#555" stroke-width="1.5"/></svg></div>
<a class="abs btn send-btn">SEND MESSAGE</a>

<div class="abs info" style="top:2364px"><svg viewBox="0 0 24 24" fill="none" stroke="#5bb046" stroke-width="1.8"><path d="M5 4h4l2 5-2.5 1.5a11 11 0 005 5L15 13l5 2v4a2 2 0 01-2 2A16 16 0 013 6a2 2 0 012-2z"/></svg>08-9120456</div>
<div class="abs info" style="top:2420px"><svg viewBox="0 0 24 24"><rect x="2" y="5" width="20" height="14" fill="#5bb046"/><path d="M2 5l10 8 10-8" fill="none" stroke="#fff" stroke-width="1.5"/></svg>hello@tavormanagement.co.il</div>
<div class="abs info" style="top:2476px"><svg viewBox="0 0 24 24"><path d="M12 2a7 7 0 00-7 7c0 5 7 13 7 13s7-8 7-13a7 7 0 00-7-7z" fill="#5bb046"/><circle cx="12" cy="9" r="2.5" fill="#fff"/></svg>Hadar Street 12, Ramat Oren</div>
<div class="abs info" style="top:2548px"><svg viewBox="0 0 24 24" fill="none" stroke="#5bb046" stroke-width="1.8"><circle cx="12" cy="12" r="9"/><path d="M3 12h18M12 3c3 3 3 15 0 18M12 3c-3 3-3 15 0 18"/></svg>https://www.tavormanagement.co.il/</div>

<!-- footer -->
<svg class="abs footer-wave" viewBox="0 0 1200 150" preserveAspectRatio="none">
  <path d="M0,30 C200,100 420,150 620,145 C850,140 1050,60 1200,40 L1200,150 L0,150 Z" fill="#000"/>
  <path d="M0,20 C200,92 420,140 620,136 C850,132 1050,52 1200,30" fill="none" stroke="#5bb046" stroke-width="8"/>
  <path d="M0,40 C200,112 420,158 620,152" fill="none" stroke="#fff" stroke-width="2"/>
</svg>
<footer class="abs footer"></footer>
<div class="abs footer-brand"><div class="brand-dot"></div><div class="brand-name">Tavor Management</div></div>
<span class="abs social" style="left:75px"></span>
<span class="abs social" style="left:114px"></span>
<span class="abs social" style="left:153px"></span>
<span class="abs social" style="left:193px"></span>
<span class="abs social" style="left:234px"></span>

<h3 class="abs foot-head" style="left:331px">ABOUT COMPANY</h3>
<ul class="abs foot-links" style="left:331px"><li>Home</li><li>About us</li><li>Services</li><li>Latest Project</li><li>Contact</li></ul>
<h3 class="abs foot-head" style="left:560px">QUCIK LINKS</h3>
<ul class="abs foot-links" style="left:560px"><li>Privacy Policy</li><li>Terms and Conditions</li><li>Sitemap</li><li>Support</li></ul>
<h3 class="abs foot-head" style="left:795px">CONTACT US</h3>
<div class="abs foot-contact" style="top:2954px"><svg viewBox="0 0 24 24" fill="none" stroke="#fff" stroke-width="1.8"><path d="M12 2a7 7 0 00-7 7c0 5 7 13 7 13s7-8 7-13a7 7 0 00-7-7z"/><circle cx="12" cy="9" r="2.5"/></svg><span>Hadar Street 12,<br>Ramat Oren</span></div>
<div class="abs foot-contact" style="top:3012px"><svg viewBox="0 0 24 24" fill="none" stroke="#fff" stroke-width="1.8"><rect x="3" y="6" width="18" height="12"/><path d="M3 6l9 7 9-7"/></svg><span>hello@tavormanagement.co.il</span></div>
<div class="abs foot-contact" style="top:3066px"><svg viewBox="0 0 24 24" fill="none" stroke="#fff" stroke-width="1.6"><path d="M5 4h4l2 5-2.5 1.5a11 11 0 005 5L15 13l5 2v4a2 2 0 01-2 2A16 16 0 013 6a2 2 0 012-2z"/></svg><span>08-9120456</span></div>
<div class="abs foot-line"></div>
<p class="abs copyright">Copyright © 2024 &nbsp;Tavor Management.. All Rights Reserved</p>
<div class="abs to-top"><svg width="24" height="24" viewBox="0 0 24 24"><circle cx="12" cy="12" r="10" fill="none" stroke="#000" stroke-width="2"/><path d="M12 18V7M7 11l5-5 5 5" fill="none" stroke="#000" stroke-width="2.4"/></svg></div>

</body>
</html>
```